Boutique holiday accommodation signage per house

I am looking for a sign to go out the front of my holiday rentals. I have just started the business and i have lots of competition so i want these signs to stand out but be elegant and modern. I need the signs to be the same but a spot for the house name to be able to be changed by me i photoshop.
Happy for suggestions of any kind.. My logo has pink in it and this is the only pink i want on the sign, happy for otherr colour suggestions but no more pink and no love hearts.
Shape - i would like to see both rectangle and circle designs
Information that needs to be on the sign

Logo - attached (can be white or black)
phone - 0491 306 284
website - www.wrenmoss.com.au
House name - The Gables (use this one for submission)
Beachfront accommodation

if you want to add property icons like shower, beds etc feel free

We live in a beachside town called Robe and its seasonal, so we are mainly accommodatio so i need to stick out!!

Target Market(s)

All ages there isnt really one - people looking for accomodation whilst driving

Industry/Entity Type

Tourism

Font styles to use
Sans Serif
Script

Requirements
Must have
• Logo - attached (can be white or black)
• phone - 0491 306 284
• website - www.wrenmoss.com.au
• House name - The Gables (use this one for submission)
• Beachfront accommodation
• i want creatvity so use your imagination
Should not have
• no hearts
• no pink

```html
<!DOCTYPE html>
<html lang="en">
<head>
<meta charset="utf-8">
<title>The Gables – Beachfront Accommodation Sign</title>
<link rel="stylesheet" href="https://fonts.googleapis.com/css2?family=Yesteryear&family=Parisienne&family=Alegreya+SC:wght@400&family=Roboto:wght@300;400;700&family=Roboto+Condensed:wght@700&display=swap">
<style>
  :root {
    --teal: #3d8ca0;
    --orange: #ee6e3b;
    --white: #ffffff;
  }
  * { margin: 0; padding: 0; box-sizing: border-box; }
  html, body { width: 1200px; height: 1000px; overflow: hidden; background: var(--white); }
  .sign {
    position: relative;
    width: 1200px;
    height: 1000px;
    background: var(--white);
  }
  .house-name {
    position: absolute;
    top: 140px;
    left: 0;
    width: 1200px;
    text-align: center;
    font-family: "Yesteryear", cursive;
    font-size: 290px;
    line-height: 1;
    color: var(--teal);
  }
  .category {
    position: absolute;
    top: 496px;
    left: 0;
    width: 1200px;
    display: flex;
    justify-content: center;
    align-items: center;
    gap: 18px;
    font-family: "Alegreya SC", serif;
    font-size: 44px;
    letter-spacing: 9px;
    color: var(--orange);
    line-height: 1;
  }
  .category .dot {
    width: 8px; height: 8px;
    background: var(--orange);
    display: inline-block;
  }
  .tagline {
    position: absolute;
    top: 582px;
    left: 0;
    width: 1200px;
    text-align: center;
    font-family: "Parisienne", cursive;
    font-size: 100px;
    line-height: 1.2;
    color: var(--orange);
  }
  .footer-band {
    position: absolute;
    left: 0;
    top: 787px;
    width: 1200px;
    height: 213px;
    background: var(--teal);
    color: var(--white);
  }
  .brand {
    position: absolute;
    left: 113px;
    top: 40px;
  }
  .brand-name {
    font-family: "Roboto Condensed", sans-serif;
    font-weight: 700;
    font-size: 92px;
    line-height: 1;
    letter-spacing: -1px;
    color: var(--white);
  }
  .brand-sub {
    font-family: "Roboto", sans-serif;
    font-weight: 300;
    font-size: 29px;
    margin-top: 8px;
    color: var(--white);
  }
  .contact {
    position: absolute;
    left: 622px;
    top: 54px;
    list-style: none;
    font-family: "Roboto", sans-serif;
    font-size: 40px;
    line-height: 46px;
  }
  .contact li { display: flex; align-items: center; gap: 18px; }
  .contact .phone { font-weight: 700; }
  .contact svg { width: 32px; height: 32px; flex: none; }
</style>
</head>
<body>
<main class="sign">
  <h1 class="house-name">The Gables</h1>
  <p class="category"><span class="dot"></span>Beachfront accommodation<span class="dot"></span></p>
  <p class="tagline">Your Next Adventure</p>

  <footer class="footer-band">
    <div class="brand">
      <div class="brand-name">WREN MOSS</div>
      <div class="brand-sub">property &amp; events management</div>
    </div>
    <ul class="contact">
      <li class="phone">
        <svg viewBox="0 0 32 32" aria-hidden="true">
          <circle cx="16" cy="16" r="15" fill="var(--white)"/>
          <path d="M11 8.5c1-.6 2-.3 2.5.6l1.4 2.6c.4.8.2 1.6-.5 2.1l-1 .7c.8 2 2.1 3.4 4 4.3l.8-1c.5-.7 1.4-.8 2.1-.4l2.5 1.5c.9.5 1.1 1.6.5 2.5l-1 1.3c-.8 1-2.3 1.3-3.6.7-4.3-2-7.3-5.2-8.7-9.6-.4-1.3 0-2.6 1-3.3z" fill="var(--teal)"/>
        </svg>
        0491 306 284
      </li>
      <li class="web">
        <svg viewBox="0 0 32 32" aria-hidden="true" fill="none" stroke="var(--white)" stroke-width="2.2">
          <circle cx="16" cy="16" r="13"/>
          <ellipse cx="16" cy="16" rx="6" ry="13"/>
          <line x1="3" y1="16" x2="29" y2="16"/>
          <line x1="5" y1="9.5" x2="27" y2="9.5"/>
          <line x1="5" y1="22.5" x2="27" y2="22.5"/>
        </svg>
        www.wrenmoss.com.au
      </li>
    </ul>
  </footer>
</main>
</body>
</html>
```